Oil & Gas Energy Consultancy Service

I am an experienced Upper Management former employed by a Global Service Company to the Oil & Gas Industry.
After 22 years I have decided to go as a Consultant working mainly in the same,(upper management) areas of work.
This is a, "One Man" operation.
Updates

Thank you all for your interest and professionalism in this little project.

It was hard to decide on a final contestant but it had to come down to one selection.
Best of luck with your other work & projects!
Tavo Ressani-Merrick

Industry/Entity Type

Industry

Contact Information for Business Card

Trelumo Energy Services, Inc
Tavo Ressani-Merrick - Managing Director
O&G Consultants
Suite 4140, Tower 3, Halden Ave, Edmonton, AB, T6K 2P5 Canada
250 555 0194 tavo.merrick@trelumo-example.net

Logo Text

Trelumo Energy Services

Logo styles of interest
Abstract Logo

```html
<!DOCTYPE html>
<html lang="en">
<head>
<meta charset="utf-8">
<title>Trelumo Energy Services – Business Card</title>
<link rel="stylesheet" href="https://fonts.googleapis.com/css2?family=Open+Sans:wght@400;600;700&family=Roboto:wght@400;500&display=swap">
<style>
  :root {
    --sky-top: #4ac4fb;
    --sky-bottom: #3aa6ea;
    --navy-band: #0d55a9;
    --label-blue: #4cc3f5;
    --title-blue: #2a7fcf;
    --ink: #111111;
    --paper: #ffffff;
  }
  html, body {
    margin: 0;
    padding: 0;
    overflow: hidden;
    background: var(--paper);
  }
  .card {
    position: relative;
    width: 1200px;
    height: 686px;
    overflow: hidden;
    background: var(--paper);
    font-family: "Roboto", Arial, sans-serif;
    color: var(--ink);
  }
  .brand-panel {
    position: absolute;
    left: 61px;
    top: 0;
    width: 505px;
    height: 366px;
    background: linear-gradient(180deg, var(--sky-top), var(--sky-bottom));
    display: flex;
    align-items: center;
    justify-content: center;
  }
  .brand-pointer {
    position: absolute;
    left: 296px;
    top: 365px;
  }
  .brand-name {
    font-family: "Open Sans", Arial, sans-serif;
    font-weight: 600;
    font-size: 34px;
    color: var(--paper);
    text-align: center;
    line-height: 1.25;
    margin: 0;
  }
  .person {
    position: absolute;
    left: 61px;
    width: 505px;
    top: 415px;
    text-align: center;
  }
  .person-name {
    font-family: "Open Sans", Arial, sans-serif;
    font-weight: 400;
    font-size: 37px;
    margin: 0;
    line-height: 1;
  }
  .person-title {
    font-family: "Open Sans", Arial, sans-serif;
    font-size: 22px;
    color: var(--title-blue);
    letter-spacing: 0.5px;
    margin: 9px 0 0;
    line-height: 1;
  }
  .divider {
    position: absolute;
    left: 628px;
    top: 183px;
  }
  .company {
    position: absolute;
    left: 667px;
    top: 164px;
    text-align: center;
  }
  .company-name {
    font-family: "Open Sans", Arial, sans-serif;
    font-weight: 400;
    font-size: 24px;
    letter-spacing: 0.3px;
    margin: 0;
    line-height: 1.1;
    white-space: nowrap;
  }
  .company-name strong { font-weight: 700; }
  .company-tagline {
    font-family: "Open Sans", Arial, sans-serif;
    font-weight: 700;
    font-size: 18px;
    margin: 0;
    line-height: 1.1;
  }
  .contact {
    position: absolute;
    left: 695px;
    top: 238px;
    margin: 0;
  }
  .contact-label {
    font-family: "Roboto", Arial, sans-serif;
    font-weight: 500;
    font-size: 16px;
    color: var(--label-blue);
    margin: 0;
    line-height: 20px;
  }
  .contact-value {
    font-size: 19.5px;
    line-height: 25px;
    margin: 0 0 22px;
  }
  .footer-band {
    position: absolute;
    left: 0;
    bottom: 0;
    width: 1200px;
    height: 77px;
    background: var(--navy-band);
  }
</style>
</head>
<body>
  <div class="card">
    <div class="brand-panel">
      <p class="brand-name">Trelumo<br>Energy Services</p>
    </div>
    <svg class="brand-pointer" width="34" height="17" viewBox="0 0 34 17" aria-hidden="true">
      <polygon points="0,0 34,0 17,17" fill="#3aa6ea"/>
    </svg>

    <div class="person">
      <p class="person-name">Tavo Ressani-Merrick</p>
      <p class="person-title">Managing Director</p>
    </div>

    <svg class="divider" width="4" height="314" viewBox="0 0 4 314" aria-hidden="true">
      <polygon points="2,0 3.5,40 3.5,274 2,314 0.5,274 0.5,40" fill="#111111"/>
    </svg>

    <div class="company">
      <p class="company-name"><strong>TRELUMO</strong> ENERGY SERVICES, INC .</p>
      <p class="company-tagline">O&amp;G Consultants</p>
    </div>

    <dl class="contact">
      <dt class="contact-label">ADDRESS</dt>
      <dd class="contact-value" style="margin-left:0">Suite 4140, Tower 3<br>Halden Ave, Edmonton, AB, T6K 2P5 Canada</dd>
      <dt class="contact-label">PHONE</dt>
      <dd class="contact-value" style="margin-left:0">250 555 0194</dd>
      <dt class="contact-label">EMAIL</dt>
      <dd class="contact-value" style="margin-left:0">tavo.merrick@trelumo-example.net</dd>
    </dl>

    <div class="footer-band"></div>
  </div>
</body>
</html>
```